Open Door Dialogues: Classroom and Family Allies building brighter pupil futures.

This is a book that helps to prepare for and hold a standard conference that an educator would have with the parents of the students in the school. It is also about how to have problem-solving conferences around difficult issues using techniques from family therapy. Parent involvement is a key ingredient for student success, but most educators have no training in holding meetings with parents. This book fills that gap.

Target Market(s)

Teachers, principals, counselors, school psychologists, school nurses. Anyone who has conferences with the parents of their students.

Font styles to use
Sans Serif

Colors
85acd3
ffcf3e

Requirements
Must have
• I have several books coming up. I'd like something that could be carried over to the new ones without too many changes. They won't all be about education. I am a psychologist so most of my writings will cover subjects related to emotional intelligence.
Nice to have
• Something dignified that will pop out for those in the schools. I like the combination of a royal blue background with white and gold (not yellow) lettering.
Should not have
• I'd like it to be easy to read. Not too messy or too much stuff on the page.

```html
<!DOCTYPE html>
<html lang="en">
<head>
<meta charset="utf-8">
<title>Open Door Dialogues – Book Cover</title>
<link href="https://fonts.googleapis.com/css2?family=Oswald:wght@500;700&family=Quicksand:wght@600&family=Montserrat:wght@500&display=swap" rel="stylesheet">
<style>
  :root {
    --stage: #1f1f1f;
    --royal-navy: #1e2a5e;
    --navy-light: #34497a;
    --navy-mist: #6e7597;
    --gold-light: #e4c45c;
    --gold-mid: #c4942f;
    --gold-deep: #a9762a;
    --paper: #eef0f3;
    --ink: #0d0d0d;
  }
  html, body {
    margin: 0;
    padding: 0;
    width: 1200px;
    height: 1200px;
    overflow: hidden;
    background: var(--stage);
  }
  .canvas {
    width: 1200px;
    height: 1200px;
    display: flex;
    align-items: center;
    justify-content: center;
  }
  .book-cover {
    width: 760px;
    height: 1140px;
    display: block;
  }
  .cover-bg { fill: var(--royal-navy); }
  .banner-white { fill: var(--paper); }
  .title-top {
    font-family: 'Oswald', sans-serif;
    font-weight: 700;
    font-size: 84px;
    fill: var(--ink);
  }
  .title-main {
    font-family: 'Oswald', sans-serif;
    font-weight: 500;
    font-size: 76px;
    letter-spacing: 3px;
    fill: var(--royal-navy);
  }
  .subtitle {
    font-family: 'Quicksand', sans-serif;
    font-weight: 600;
    font-size: 22px;
    letter-spacing: 0.5px;
    fill: var(--ink);
  }
  .author-name {
    font-family: 'Montserrat', sans-serif;
    font-weight: 500;
    font-size: 20px;
    letter-spacing: 4px;
    fill: var(--royal-navy);
  }
</style>
</head>
<body>
<main class="canvas">
  <svg class="book-cover" viewBox="0 0 760 1140" xmlns="http://www.w3.org/2000/svg" aria-labelledby="cover-title">
    <title id="cover-title">Open Door Dialogues: Classroom and Family Allies building brighter pupil futures</title>
    <defs>
      <linearGradient id="gold-foil" x1="0" y1="0" x2="1" y2="0">
        <stop offset="0" stop-color="var(--gold-light)"/>
        <stop offset="0.35" stop-color="var(--gold-deep)"/>
        <stop offset="0.75" stop-color="var(--gold-light)"/>
        <stop offset="1" stop-color="var(--gold-mid)"/>
      </linearGradient>
      <linearGradient id="cover-sheen" x1="0" y1="0" x2="1" y2="1">
        <stop offset="0" stop-color="#ffffff" stop-opacity="0.22"/>
        <stop offset="0.35" stop-color="#ffffff" stop-opacity="0"/>
      </linearGradient>
      <linearGradient id="mic-tones" x1="0" y1="1" x2="1" y2="0">
        <stop offset="0" stop-color="var(--paper)"/>
        <stop offset="1" stop-color="var(--gold-mid)"/>
      </linearGradient>
      <linearGradient id="seat-tones" x1="0" y1="0" x2="0" y2="1">
        <stop offset="0" stop-color="var(--navy-light)"/>
        <stop offset="0.18" stop-color="var(--navy-mist)"/>
        <stop offset="0.32" stop-color="var(--paper)"/>
        <stop offset="1" stop-color="var(--paper)"/>
      </linearGradient>
    </defs>

    <rect class="cover-bg" x="0" y="0" width="760" height="1140"/>
    <rect x="0" y="0" width="760" height="1140" fill="url(#cover-sheen)"/>

    <rect class="emblem-area" role="img" aria-label="Microphone on a stand, white with gold head"
          x="330" y="190" width="170" height="210" rx="22" fill="url(#mic-tones)" opacity="0.85"/>

    <g class="title-ribbon" transform="rotate(-9 400 550)">
      <polygon class="banner-gold" fill="url(#gold-foil)" points="190,400 680,400 620,505 130,505"/>
      <polygon class="banner-white" points="150,505 665,505 700,600 95,600 140,552"/>
      <polygon class="banner-gold" fill="url(#gold-foil)" points="190,600 690,600 620,700 130,700"/>

      <text class="title-top" x="410" y="488" text-anchor="middle">Open Door</text>
      <text class="title-main" x="400" y="586" text-anchor="middle">DIALOGUES</text>
      <text class="subtitle" x="410" y="640" text-anchor="middle">Classroom and Family Allies building</text>
      <text class="subtitle" x="400" y="672" text-anchor="middle">brighter pupil futures</text>
    </g>

    <rect class="seating-area" role="img" aria-label="Rows of audience seats facing the stage"
          x="0" y="870" width="760" height="270" fill="url(#seat-tones)"/>

    <text class="author-name" x="380" y="1075" text-anchor="middle">AUTHOR NAME</text>
  </svg>
</main>
</body>
</html>
```